File your income taxes and walk away with cash today. direct mailer campaign

We prepare income tax returns. Our slogan is Walk away with cash today! Our marketing edge above our competition is the fact that clients can get up to $5000 the day they file. We also offer notary, payroll, and bookkeeping services. We would like something with cash on the card as well. Quill Ledger Returns is the name of our company and this campaign is actually for a direct mailer to client prospects that make under 25k a year, who will be looking for help preparing their income tax documents but also be looking for cash the same day they file. Our office will begin handing out checks on January 2nd!

Target Market(s)

My target market for this particular piece is Blacks and Hispanics of lower income.

Industry/Entity Type

Finance And Accounting

Font styles to use
Serif
Script

Colors
a54499
b768aa
33a6d7
33b8a4
e667a6
e34197

Requirements
Must have
• Quill Ledger Returns should be written is some form of script, prefer colors of Purple & aqua or Pink and Turquoise. Some form of cash that looks as real as possible.
Nice to have
• Here is our contact info:
• 412 North Caldwell Hammond Parkway
• Dallas, TX 75148
• (281) 555-0374
• www.quillledgerreturns.example
Should not have
• No white people or body parts

```html
<!DOCTYPE html>
<html lang="en">
<head>
<meta charset="utf-8">
<title>Quill Ledger Returns – Walk Away With Cash Today</title>
<link rel="stylesheet" href="https://fonts.googleapis.com/css2?family=Abril+Fatface&family=Dancing+Script:wght@700&family=Lora:wght@400;700&display=swap">
<style>
  :root {
    --purple: #a54499;
    --orchid: #b768aa;
    --aqua: #33a6d7;
    --teal: #33b8a4;
    --pink: #e34197;
    --rose: #e667a6;
    --ink: #1f1a24;
    --paper: #ffffff;
    --stage: #000000;
    --cash-light: #dfe6d2;
    --cash-mid: #9fb48f;
    --cash-dark: #4f6b4c;
  }
  * { box-sizing: border-box; margin: 0; padding: 0; }
  html, body {
    width: 1200px; height: 859px; overflow: hidden;
    background: var(--stage);
  }
  .stage {
    width: 1200px; height: 859px;
    display: flex; justify-content: center; align-items: center; gap: 24px;
  }
  .mailer {
    width: 504px; height: 648px;
    background: var(--paper); overflow: hidden;
    display: flex; flex-direction: column;
    font-family: "Lora", serif; color: var(--ink);
  }
  .headline { font-weight: 400; }
  .headline-lead {
    display: block;
    font-family: "Dancing Script", cursive; font-weight: 700;
    color: var(--purple); font-size: 40px; line-height: 1.05;
  }
  .headline-main {
    display: block;
    font-family: "Abril Fatface", serif; color: var(--pink);
    font-size: 64px; line-height: 1.02; letter-spacing: 0.5px;
  }
  .pitch { font-size: 19px; line-height: 1.32; margin-top: 4px; }
  .pitch strong { font-weight: 700; color: var(--purple); }
  .cash-photo {
    background:
      linear-gradient(160deg, var(--cash-light) 0%, var(--cash-mid) 50%, var(--cash-dark) 100%);
  }
  .brand-name {
    font-family: "Dancing Script", cursive; font-weight: 700;
    color: var(--purple); line-height: 1;
  }

  /* front */
  .front .intro { padding: 20px 18px 0; height: 200px; }
  .front .cash-photo { height: 280px; flex: none; }
  .front .services { position: relative; height: 40px; flex: none; margin-top: -20px; }
  .front .services svg { position: absolute; inset: 0; width: 100%; height: 100%; }
  .front .services-text {
    position: absolute; left: 16px; top: 17px;
    color: #fff; font-size: 13px; white-space: nowrap;
    transform: rotate(-1.6deg); transform-origin: left center;
  }
  .services-text strong { font-weight: 700; }
  .front .footer {
    flex: 1; display: flex; justify-content: space-between; align-items: center;
    padding: 6px 18px 10px 28px;
  }
  .front .brand-name { font-size: 46px; }
  .contact { text-align: right; font-size: 12px; }
  .contact .call-label { font-size: 11px; text-transform: uppercase; letter-spacing: 0.5px; color: var(--purple); }
  .contact .phone { color: var(--pink); font-weight: 700; font-size: 22px; line-height: 1.15; }
  .contact .line { display: flex; align-items: center; justify-content: flex-end; gap: 4px; margin-top: 2px; }

  /* back */
  .back .cash-photo { position: relative; height: 370px; flex: none; }
  .back .brand-tag {
    position: absolute; left: 0; top: 30px;
    background: var(--purple); padding: 10px 16px 12px;
  }
  .back .brand-tag .brand-name { color: #fff; font-size: 34px; }
  .back .intro { padding: 14px 16px 0; flex: 1; }
  .back .pitch { font-size: 20px; }
  .back .services-band {
    height: 42px; flex: none;
    background: linear-gradient(90deg, var(--aqua), var(--teal));
    color: #fff; font-size: 15px;
    display: flex; align-items: center; justify-content: center; gap: 5px;
  }
</style>
</head>
<body>
<main class="stage">

  <article class="mailer front">
    <header class="intro">
      <h1 class="headline">
        <span class="headline-lead">Walk away with</span>
        <span class="headline-main">CASH TODAY!</span>
      </h1>
      <p class="pitch">Our customer catch is the fact that they<br>can get up to <strong>$5000</strong> the day they file.</p>
    </header>
    <div class="cash-photo" role="img" aria-label="Fanned stack of US dollar bills held out in an open hand"></div>
    <div class="services">
      <svg viewBox="0 0 504 40" preserveAspectRatio="none" aria-hidden="true">
        <polygon points="330,8 504,0 504,28 345,32" fill="var(--aqua)"/>
        <polygon points="0,20 340,8 352,32 0,40" fill="var(--pink)"/>
      </svg>
      <p class="services-text">We also offer <strong>Notary, Payroll &amp; Bookkeeping Services.</strong></p>
    </div>
    <footer class="footer">
      <div class="brand-name">Quill Ledger<br>Returns</div>
      <div class="contact">
        <div class="call-label">Call us</div>
        <div class="phone">(281) 555-0374</div>
        <div class="line">
          <svg width="11" height="9" viewBox="0 0 11 9" aria-hidden="true"><rect x="0.5" y="0.5" width="10" height="8" fill="none" stroke="#1f1a24"/><path d="M0.5 0.5 L5.5 5 L10.5 0.5" fill="none" stroke="#1f1a24"/></svg>
          info@quillledgerreturns.example
        </div>
        <div class="line">
          <svg width="11" height="11" viewBox="0 0 11 11" aria-hidden="true"><circle cx="5.5" cy="5.5" r="5" fill="none" stroke="#1f1a24"/><ellipse cx="5.5" cy="5.5" rx="2.2" ry="5" fill="none" stroke="#1f1a24"/><line x1="0.5" y1="5.5" x2="10.5" y2="5.5" stroke="#1f1a24"/></svg>
          www.quillledgerreturns.example
        </div>
      </div>
    </footer>
  </article>

  <article class="mailer back">
    <div class="cash-photo" role="img" aria-label="Close-up of crisp hundred dollar bills spread in a fan">
      <div class="brand-tag"><div class="brand-name">Quill Ledger<br>Returns</div></div>
    </div>
    <div class="intro">
      <h2 class="headline">
        <span class="headline-lead">Walk away with</span>
        <span class="headline-main">CASH TODAY!</span>
      </h2>
      <p class="pitch">Our customer catch is the fact that they<br>can get up to <strong>$5000</strong> the day they file.</p>
    </div>
    <p class="services-band">We also offer <strong>Notary, Payroll &amp; Bookkeeping Services.</strong></p>
  </article>

</main>
</body>
</html>
```